Custom Cabinet Shop Needs a website design

Hi,
We need a website for a Custom Cabinet Shop and Cabinet parts manufacturing business.
The business has two sides to it. One side provides custom Kitchens, vanities, entertainment units, offices and what not to homeowners and contractors.
The 2nd side of the business provides built to order cabinet boxes and other parts required to put together a project to other cabinet shops, small contractors looking to install there own cabinets.
Website will need a Gallery to display work.
Color scheme to go well with logo.
current website is www.brindlewoodcustomcabinets.com
being changed to www.brindlewood.ca
Logo Included in attached files.
Tagline "Millwork with Flare"
Mission Statement "Our passion is to deliver inspired cabinetry solutions to suit all your needs, supported by our phenomenal star class customer service"
The website should convey quality and professionalism.
Thank you.
Homeowners/ Contractors
Entertainment
Coded - Design and coding required
1 page

```html
<!DOCTYPE html>
<html lang="en">
<head>
<meta charset="utf-8">
<title>Brindlewood Custom Cabinets</title>
<link href="https://fonts.googleapis.com/css2?family=Source+Sans+3:wght@400;600;700&display=swap" rel="stylesheet">
<style>
:root{
  --orange:#f05a22;
  --orange-dark:#c9400f;
  --ink:#3a3a3a;
  --muted:#6b6b6b;
  --line:#e2e2e2;
  --band:#f4f4f4;
  --white:#ffffff;
}
*{box-sizing:border-box;margin:0;padding:0}
html,body{width:720px;height:1200px;overflow:hidden;background:var(--white)}
body{font-family:"Source Sans 3",Arial,sans-serif;color:var(--ink);position:relative}
.abs{position:absolute}
.topbar{left:0;top:0;width:720px;height:18px;background:#f6f6f6;border-bottom:1px solid #ececec}
.social{display:flex;gap:6px}
.social span{width:9px;height:9px;border-radius:50%;background:#555}
.topbar .social{right:146px;top:4px}
.brand{left:108px;top:40px;display:flex;align-items:center;gap:6px;font-size:19px;font-weight:700;color:var(--ink);letter-spacing:.5px}
.brand i{width:12px;height:12px;background:var(--orange);display:block}
.nav{left:384px;top:44px;display:flex;gap:0;font-size:6px;text-transform:uppercase;color:#777}
.nav a{display:block;padding:4px 9px;margin-right:12px;text-decoration:none;color:#777}
.nav a.active{background:var(--orange);color:var(--white)}
.hero{left:0;top:98px;width:720px;height:182px;background:linear-gradient(90deg,#d9d9d9 0%,#c9c9c9 30%,#6e2418 45%,#5a1c12 70%,#cfd3c8 85%,#e0e0e0 100%)}
.hero-arrow{top:72px;width:27px;height:40px;background:var(--white);display:flex;align-items:center;justify-content:center}
.dots{display:flex;gap:7px}
.dots span{width:9px;height:9px;border-radius:50%;border:2px solid #aaa;background:#eee}
.feature{top:333px;width:180px;text-align:center}
.feature .ring{width:62px;height:62px;margin:0 auto;border-radius:50%;border:1px solid #e5e5e5;display:flex;align-items:center;justify-content:center}
.feature h3{font-size:11.5px;font-weight:400;margin:12px 0 8px;letter-spacing:.3px}
.feature p{font-size:7.4px;line-height:14px;color:var(--muted)}
.feature .more{font-size:7.6px;margin-top:10px;color:var(--ink)}
.band{left:0;top:526px;width:720px;height:222px;background:var(--band)}
.h-orange{font-size:11px;font-weight:600;color:var(--orange);text-transform:uppercase}
.sub{font-size:5.8px;color:var(--muted)}
.rule{height:1px;background:var(--line)}
.rule b{position:absolute;right:0;top:-1px;width:14px;height:2px;background:var(--orange)}
.small{font-size:5.4px;line-height:10.3px;color:var(--muted)}
.stars{display:flex;gap:2px}
.stars span{width:6px;height:6px;background:#f2b600;clip-path:polygon(50% 0,61% 35%,98% 35%,68% 57%,79% 91%,50% 70%,21% 91%,32% 57%,2% 35%,39% 35%)}
.photo{background:linear-gradient(135deg,#c9a27a,#8c6a4c)}
.avatar{left:458px;top:602px;width:52px;height:52px;border-radius:50%;background:linear-gradient(#d8c2ad,#9d8775);border:2px solid #fff}
.product{top:830px;width:104px;text-align:center}
.product .img{height:98px;margin:0 8px}
.product .name{font-size:6.6px;color:#555;margin-top:12px}
.product .price{font-size:6.6px;color:#555;margin-top:4px}
.footer{left:0;top:1005px;width:720px;height:195px;background:var(--orange);color:var(--white)}
.footer h4{font-size:8px;font-weight:700;text-transform:uppercase}
.footer .frule{height:1px;background:rgba(255,255,255,.25)}
.tweet b{font-size:6.4px;font-weight:700}
.tweet em{font-style:normal;font-size:4.6px;margin-left:26px}
.tweet p{font-size:5.1px;line-height:10.3px;margin-top:3px}
.thumb{width:30px;height:30px;border:2px solid #f4d8cc;background:linear-gradient(#8a8f95 50%,#b98a55 50%)}
.field{left:464px;width:112px;background:var(--orange-dark);border-radius:2px;font-size:5.6px;padding:5px 9px}
.submit{left:540px;top:1144px;width:36px;height:12px;background:var(--orange-dark);font-size:5px;font-weight:700;text-align:center;line-height:12px}
.copy{left:106px;top:1178px;font-size:5.2px}
.footer .social span{background:rgba(255,255,255,.8)}
</style>
</head>
<body>
<header>
  <div class="abs topbar">
    <div class="abs social"><span></span><span></span><span></span><span></span></div>
  </div>
  <div class="abs brand"><i></i>BRINDLEWOOD</div>
  <nav class="abs nav">
    <a class="active" href="#">Home</a><a href="#">Gallery</a><a href="#">Service</a><a href="#">About</a><a href="#">Contact</a>
  </nav>
</header>

<section class="abs hero" role="img" aria-label="Kitchen with dark wood cabinets and cream countertop">
  <div class="abs hero-arrow" style="left:0"><svg width="8" height="12"><path d="M6 1 1 6l5 5" fill="none" stroke="#444" stroke-width="1.4"/></svg></div>
  <div class="abs hero-arrow" style="right:0"><svg width="8" height="12"><path d="M2 1l5 5-5 5" fill="none" stroke="#444" stroke-width="1.4"/></svg></div>
  <div class="abs dots" style="left:337px;top:160px"><span></span><span></span><span></span></div>
</section>

<section>
  <div class="abs feature" style="left:73px">
    <div class="ring"><svg width="26" height="30"><rect x="2" y="2" width="22" height="26" fill="none" stroke="#f05a22" stroke-width="2"/><line x1="13" y1="2" x2="13" y2="28" stroke="#f05a22" stroke-width="1.5"/><line x1="2" y1="20" x2="24" y2="20" stroke="#f05a22" stroke-width="1.5"/></svg></div>
    <h3>PRODUCT</h3>
    <p>Our passion is to deliver inspired cabinetry solu-<br>tions to suit all your needs, supported by our phe-<br>nomenal star class customer service</p>
    <div class="more">Read more</div>
  </div>
  <div class="abs feature" style="left:270px">
    <div class="ring"><svg width="30" height="26"><g fill="#f05a22"><circle cx="6" cy="5" r="3"/><circle cx="15" cy="4" r="3"/><circle cx="24" cy="5" r="3"/><rect x="3" y="10" width="6" height="15" rx="2"/><rect x="12" y="9" width="6" height="16" rx="2"/><rect x="21" y="10" width="6" height="15" rx="2"/></g></svg></div>
    <h3>SERVICES</h3>
    <p>Our passion is to deliver inspired cabinetry solu-<br>tions to suit all your needs, supported by our phe-<br>nomenal star class customer service</p>
    <div class="more">Read more</div>
  </div>
  <div class="abs feature" style="left:462px">
    <div class="ring"><svg width="24" height="30"><path d="M5 14V5a2 2 0 0 1 4 0v7V3a2 2 0 0 1 4 0v9V4a2 2 0 0 1 4 0v10l2-3a2 2 0 0 1 3 2l-5 9c-2 4-4 6-8 6-4 0-6-3-6-7z" fill="#f05a22"/></svg></div>
    <h3 style="margin-top:3px">MISSION</h3>
    <p style="margin-top:17px">Our passion is to deliver inspired cabinetry solu-<br>tions to suit all your needs, supported by our phe-<br>nomenal star class customer service</p>
    <div class="more">Read more</div>
  </div>
</section>

<section class="abs band"></section>
<section>
  <h2 class="abs h-orange" style="left:103px;top:541px">Featured Product</h2>
  <p class="abs sub" style="left:104px;top:562px">Vestibulum ac diam sit amet quam vehicula elementum sed sit amet dui.</p>
  <div class="abs rule" style="left:103px;top:584px;width:235px"></div>
  <div class="abs stars" style="left:103px;top:595px"><span></span><span></span><span></span><span></span></div>
  <div class="abs small" style="left:150px;top:593px">Section - A</div>
  <div class="abs" style="left:310px;top:593px;font-size:7px">$ 5984</div>
  <div class="abs rule" style="left:103px;top:610px;width:235px"></div>
  <div class="abs photo" style="left:105px;top:622px;width:88px;height:50px" role="img" aria-label="Light wood kitchen cabinets"></div>
  <p class="abs small" style="left:198px;top:619px;width:140px;text-align:justify">Cras ultricies ligula sed magna dictum porta. Pellentesque in ipsum id orci porta dapibus. Vivamus magna justo, lacinia eget consectetur sed, convallis at tellus. Mauris blandit aliquet elit, eget tincidunt nibh pulvinar a. Lorem ipsum dolor sit</p>
  <p class="abs small" style="left:104px;top:676px;width:234px;text-align:justify">Cras ultricies ligula sed magna dictum porta. Pellentesque in ipsum id orci porta dapibus. Pellentesque in ipsum id orci porta dapibus. Vivamus magna justo, lacinia eget consectetur sed, convallis at tellus. Mauris blandit aliquet elit, eget tincidunt nibh pulvinar a. Lorem ipsum dolor sit amet,</p>

  <h2 class="abs h-orange" style="left:360px;top:541px">Testimonials</h2>
  <p class="abs sub" style="left:361px;top:562px">Vestibulum ac diam sit amet quam vehicula elementum sed sit amet dui.</p>
  <div class="abs rule" style="left:360px;top:584px;width:254px"><b></b></div>
  <div class="abs avatar" role="img" aria-label="Customer portrait"></div>
  <p class="abs small" style="left:362px;top:661px;width:250px;text-align:center">Vivamus magna justo, lacinia eget consectetur sed, convallis at tellus. Donec rutrum congue leo eget malesuada. Donec rutrum congue leo eget malesuada. Vestibulum ac diam sit amet quam vehicula elementum sed sit amet dui. Donec rutrum congue leo</p>
  <div class="abs" style="left:440px;top:701px;width:90px;text-align:center;font-size:4.8px;font-weight:700;font-style:italic;line-height:10px">DANIEL MARSH<br>CEO OF OAKLINE</div>
  <div class="abs dots" style="left:578px;top:708px;gap:5px"><span style="width:8px;height:8px;border-width:1.5px;border-color:#ccc"></span><span style="width:8px;height:8px;border-width:1.5px;border-color:#ccc"></span><span style="width:8px;height:8px;border-width:1.5px;border-color:#ccc"></span></div>
</section>

<section>
  <h2 class="abs h-orange" style="left:0;width:720px;text-align:center;top:773px">Some of our products</h2>
  <p class="abs sub" style="left:0;width:720px;text-align:center;top:794px">Vestibulum ac diam sit amet quam vehicula elementum sed sit amet dui.</p>
  <div class="abs rule" style="left:103px;top:812px;width:511px"><b></b></div>
  <svg class="abs" style="left:64px;top:892px" width="10" height="16"><path d="M8 1 2 8l6 7" fill="none" stroke="#f05a22" stroke-width="2"/></svg>
  <svg class="abs" style="left:648px;top:892px" width="10" height="16"><path d="M2 1l6 7-6 7" fill="none" stroke="#f05a22" stroke-width="2"/></svg>
  <div class="abs product" style="left:100px"><div class="img" style="background:linear-gradient(#fff 25%,#4a2a1c 25%,#4a2a1c 80%,#fff 80%)" role="img" aria-label="Dark wood sideboard"></div><div class="name">Alder-Ridge-Sideboard</div><div class="price">$598</div></div>
  <div class="abs product" style="left:208px"><div class="img" style="margin:0 22px;background:linear-gradient(#2d2a26,#3b3430)" role="img" aria-label="Glass-front black china cabinet"></div><div class="name">Alder-Ridge-Sideboard</div><div class="price">$598</div></div>
  <div class="abs product" style="left:320px"><div class="img" style="background:linear-gradient(#fff 10%,#eeeeee 10%,#e6e6e6 90%,#fff 90%)" role="img" aria-label="White storage cabinet"></div><div class="name">Alder-Ridge-Sideboard</div><div class="price">$598</div></div>
  <div class="abs product" style="left:421px"><div class="img" style="margin:0 32px;background:linear-gradient(#9fa3a3,#7d8282)" role="img" aria-label="Tall grey glass cabinet"></div><div class="name">Alder-Ridge-Sideboard</div><div class="price">$598</div></div>
  <div class="abs product" style="left:532px"><div class="img" style="margin:0 12px;background:linear-gradient(90deg,#8b7355,#a68b63 40%,#d8b340 50%,#a68b63 60%,#8b7355)" role="img" aria-label="Rustic wood armoire"></div><div class="name">Alder-Ridge-Sideboard</div><div class="price">$598</div></div>
</section>

<footer class="abs footer">
  <h4 class="abs" style="left:104px;top:27px">Latest Tweets</h4>
  <div class="abs frule" style="left:104px;top:46px;width:146px"></div>
  <div class="abs tweet" style="left:104px;top:55px;width:146px"><b>TOM ELLERY</b><em>- Posted 20-11-2015</em><p>Vestibulum ante ipsum primis in faucibus orci luctus et ultrices posuere cubilia Curae; Donec velit neque, auctor sit amet aliquam vel, ullamcorper sit amet ligula. Lorem</p></div>
  <div class="abs tweet" style="left:104px;top:109px;width:146px"><b>TOM ELLERY</b><em>- Posted 20-11-2015</em><p>Vestibulum ante ipsum primis in faucibus orci luctus et ultrices posuere cubilia Curae; Donec velit neque, auctor sit amet aliquam vel, ullamcorper sit amet ligula. Lorem</p></div>

  <h4 class="abs" style="left:271px;top:27px">Flicker Gallery</h4>
  <div class="abs frule" style="left:271px;top:46px;width:170px"></div>
  <p class="abs" style="left:271px;top:49px;width:150px;font-size:5.1px;line-height:10.3px">Vestibulum ante ipsum primis in faucibus orci luctus et ultrices posuere cubilia Curae; Donec velit neque, auctor</p>
  <div class="abs" style="left:271px;top:83px;display:grid;grid-template-columns:repeat(4,30px);gap:6px 6px" role="img" aria-label="Gallery thumbnails of finished kitchens">
    <div class="thumb"></div><div class="thumb"></div><div class="thumb"></div><div class="thumb"></div>
    <div class="thumb"></div><div class="thumb"></div><div class="thumb"></div><div class="thumb"></div>
  </div>

  <h4 class="abs" style="left:466px;top:27px">Contact Us</h4>
  <div class="abs frule" style="left:464px;top:46px;width:152px"></div>
  <div class="abs field" style="top:54px;height:17px">Your Full Name</div>
  <div class="abs field" style="top:77px;height:17px">E-mail</div>
  <div class="abs field" style="top:98px;height:35px">Message</div>
  <div class="abs submit" style="top:139px">SUBMIT</div>

  <div class="abs copy" style="top:173px">Copyright (c) at harrowlane.com 2014-2015</div>
  <div class="abs social" style="left:518px;top:176px"><span></span><span></span><span></span><span></span></div>
</footer>
</body>
</html>
```